Harbor Nightclub

Nightclub flyer., digital single sided, for KV and PX. I included samples of some previous flyers we've used. Sample Info:
HARBOR
FRIDAYS
FRI MAY 1 2020
DJ VORTAN (club floor)
DJ RUZO & DJ TAV (residents on the lounge floor)
4217 Marlow Avenue Sacramento
www.harborvenuehall.example for list/VIP inquiries

Target Market(s)

Upscale top 40 crowd but want some cool and artsy like the examples included.

Font styles to use
Sans Serif

Requirements
Must have
• Harbor Logo
Nice to have
• Would be nice if the flyer can be incorporated later with DJ photos (sometimes we will add dj photos to pixagram etc). Would like a big city type of feel.
Should not have
• Nothing too sexual.

```html
<!DOCTYPE html>
<html lang="en">
<head>
<meta charset="utf-8">
<title>Harbor Fridays</title>
<link href="https://fonts.googleapis.com/css2?family=Oswald:wght@300;400&family=Montserrat:wght@400;500&display=swap" rel="stylesheet">
<style>
  :root {
    --night: #07060c;
    --neon-pink: #e23cf0;
    --white: #ffffff;
    --silver: #d9d9dc;
    --silver-dark: #8e8e94;
    --frame-yellow: #e4ee3a;
    --gold: #b9a55a;
  }
  * { margin: 0; padding: 0; box-sizing: border-box; }
  html, body { width: 960px; height: 1200px; overflow: hidden; background: var(--night); }
  .flyer { position: relative; width: 960px; height: 1200px; overflow: hidden; background: var(--night); font-family: "Montserrat", sans-serif; color: var(--white); }
  .backdrop { position: absolute; inset: 0;
    background:
      radial-gradient(ellipse 420px 260px at 420px 820px, rgba(120,90,30,0.35), transparent 70%),
      radial-gradient(ellipse 600px 400px at 300px 200px, rgba(40,40,90,0.45), transparent 75%),
      radial-gradient(ellipse 500px 500px at 800px 300px, rgba(30,30,70,0.4), transparent 75%),
      linear-gradient(180deg, #0b0a18 0%, #0a0a14 55%, #120f0a 85%, #07060c 100%); }
  .glow { position: absolute; left: 150px; top: 50px; width: 660px; height: 300px;
    background: radial-gradient(ellipse 50% 48% at 50% 55%, rgba(226,60,240,0.75) 0%, rgba(226,60,240,0.35) 45%, transparent 75%);
    filter: blur(6px); }
  .night-title { position: absolute; left: 0; width: 960px; top: 121px; text-align: center;
    font-family: "Oswald", sans-serif; font-weight: 400; font-size: 216px; line-height: 1; letter-spacing: 2px;
    transform: scaleX(0.86); transform-origin: 50% 0;
    color: var(--white); text-shadow: 0 0 10px var(--neon-pink), 0 0 26px var(--neon-pink); }
  .venue-name { position: absolute; left: 0; width: 960px; top: 369px; text-align: center; line-height: 1;
    font-size: 37px; font-weight: 500; letter-spacing: 0.9em; padding-left: 0.9em; }
  .event-date { position: absolute; left: 0; width: 960px; top: 410px; text-align: center; line-height: 1;
    font-size: 35px; font-weight: 500; letter-spacing: 0.14em; padding-left: 0.14em; }
  .lineup-art { position: absolute; left: 0; top: 0; width: 960px; height: 1200px; }
  .dj { position: absolute; font-family: "Oswald", sans-serif; font-weight: 300; line-height: 1; white-space: nowrap;
    transform-origin: 0 0;
    background: linear-gradient(180deg, var(--white) 0%, var(--silver) 45%, var(--silver-dark) 100%);
    -webkit-background-clip: text; background-clip: text; color: transparent; }
  .dj--headliner { left: 119px; top: 539px; font-size: 110px; letter-spacing: 1px; transform: scaleX(0.9); }
  .dj--residents { left: 331px; top: 822px; font-size: 108px; letter-spacing: 1px; transform: scaleX(0.68); }
  .venue-mark { position: absolute; left: 455px; top: 963px; width: 50px; height: 50px; border-radius: 50%; background: var(--gold); }
  .venue-wordmark { position: absolute; left: 0; width: 960px; top: 1038px; text-align: center; line-height: 1; font-size: 32px; font-weight: 500; letter-spacing: 0.04em; color: var(--silver); }
  .address { position: absolute; left: 0; width: 960px; top: 1087px; text-align: center; line-height: 1; font-size: 21px; letter-spacing: 0.42em; padding-left: 0.42em; }
  .rule { position: absolute; left: 303px; top: 1131px; width: 374px; height: 1px; background: rgba(255,255,255,0.6); }
  .website { position: absolute; left: 0; width: 960px; top: 1145px; text-align: center; line-height: 1; font-size: 20px; letter-spacing: 0.26em; padding-left: 0.26em; }
</style>
</head>
<body>
<div class="flyer">
  <div class="backdrop" role="img" aria-label="Dark night photograph of a waterfall among trees"></div>
  <div class="glow"></div>
  <div class="night-title">FRIDAY</div>
  <div class="venue-name">HARBOR</div>
  <div class="event-date">MAY•01•2020</div>

  <svg class="lineup-art" viewBox="0 0 960 1200" xmlns="http://www.w3.org/2000/svg">
    <defs>
      <linearGradient id="scene" x1="0" y1="0" x2="0" y2="1">
        <stop offset="0" stop-color="#5a3aa8"/>
        <stop offset="0.45" stop-color="#4a4d66"/>
        <stop offset="0.8" stop-color="#8c7430"/>
        <stop offset="1" stop-color="#b89a3c"/>
      </linearGradient>
    </defs>
    <g class="frame" fill="none" stroke="#e4ee3a" stroke-width="2.5">
      <polyline points="94,940 94,507 697,507"/>
      <line x1="863" y1="673" x2="863" y2="940"/>
    </g>
    <g class="scene-tiles" fill="url(#scene)" stroke="#e4ee3a" stroke-width="1">
      <polygon role="img" aria-label="Waterfall photo with violet foliage" points="127,683 211,680 262,745 287,848 231,915 167,930 62,888 33,777"/>
      <polygon role="img" aria-label="Waterfall photo with violet foliage" points="332,648 404,645 460,686 479,772 457,808 359,837 303,812 287,735"/>
      <polygon role="img" aria-label="Waterfall photo with violet foliage" points="531,613 630,610 680,661 693,737 677,788 593,817 504,796 481,706"/>
      <polygon role="img" aria-label="Waterfall photo with violet foliage" points="701,466 837,463 893,515 910,547 892,650 773,710 669,675 660,560"/>
    </g>
  </svg>

  <div class="dj dj--headliner">DJ VORTAN</div>
  <div class="dj dj--residents">DJ RUZO &amp; DJ TAV</div>

  <div class="venue-mark"></div>
  <div class="venue-wordmark">HARBOR</div>
  <div class="address">4217 MARLOW AVENUE SACRAMENTO</div>
  <div class="rule"></div>
  <div class="website">WWW.HARBORVENUEHALL.EXAMPLE</div>
</div>
</body>
</html>
```